Meadowrun Honey labels

I have honey farm . I would like to sale it at grocery stores. I need really unique and very attractive designed labels, I would like to see writings 100% Natural honey and GMO free ,. Company name "MeadowrunHoney" . I want to put 2 labels and one ribbon tag in middle and round label on top of lid(only one diamond shape in the middle).I would like to see bee flying over red flower and at the left side flower field and right side bee putting honey into honey hives. I have attached example pictures of Honey Jars labels, tags and type. I have two different type of Honey jars i have also attached picture of those jars. For jar with red lid. If middle label little bit bigger than measurement thats ok because writing has to fit.

Target Market(s)

Grocery stores

Industry/Entity Type

Farm

Requirements
Must have
• 100% Natural Honey, GMO Free, Company name Meadowrun Honey, attractive and unique design. bee flying over flower, right side label flower field left side bee putting honey into bee hives.

```html
<!DOCTYPE html>
<html lang="en">
<head>
<meta charset="utf-8">
<title>Meadowrun Honey – Ribbon Labels</title>
<link href="https://fonts.googleapis.com/css2?family=Open+Sans:wght@400;600;700&display=swap" rel="stylesheet">
<style>
  :root {
    --page: #ffffff;
    --black-band: #000000;
    --black-comb: #262626;
    --red-band: #a63636;
    --red-comb: #b24444;
    --yellow-band: #fdc313;
    --yellow-comb: #ffd23f;
    --gold: #f8c51b;
    --gold-deep: #e0a800;
    --white: #ffffff;
    --cream: #fff3cc;
    --ink: #111111;
  }
  html, body {
    margin: 0;
    padding: 0;
    width: 1200px;
    height: 915px;
    overflow: hidden;
    background: var(--page);
    font-family: "Open Sans", Arial, sans-serif;
  }
  .sheet {
    position: relative;
    width: 1200px;
    height: 915px;
  }
  .ribbon-label {
    position: absolute;
    left: 0;
    width: 1200px;
    height: 262px;
  }
  .ribbon-label--black  { top: 25px;  --band: var(--black-band);  --comb: var(--black-comb);  --name: var(--white); --accent: var(--gold);  --hive: var(--gold);  --hive-deep: var(--gold-deep); --note: var(--white); }
  .ribbon-label--red    { top: 338px; --band: var(--red-band);    --comb: var(--red-comb);    --name: var(--white); --accent: var(--gold);  --hive: var(--gold);  --hive-deep: var(--gold-deep); --note: var(--white); }
  .ribbon-label--yellow { top: 634px; --band: var(--yellow-band); --comb: var(--yellow-comb); --name: var(--ink);   --accent: var(--white); --hive: var(--white); --hive-deep: var(--cream);     --note: var(--ink); }

  .band {
    position: absolute;
    left: 15px;
    top: 67px;
    width: 1175px;
    height: 128px;
    background:
      linear-gradient(90deg, var(--band) 0%, var(--comb) 25%, var(--band) 50%, var(--comb) 75%, var(--band) 100%);
  }
  .badge {
    position: absolute;
    left: 492px;
    top: 0;
    width: 216px;
    height: 262px;
  }
  .badge__shape { fill: var(--band); }
  .badge__text {
    position: absolute;
    left: 0;
    width: 216px;
    margin: 0;
    text-align: center;
  }
  .brand-name {
    top: 50px;
    font-weight: 700;
    font-size: 27px;
    line-height: 32px;
    color: var(--name);
  }
  .hive-art {
    position: absolute;
    left: 56px;
    top: 124px;
    width: 104px;
    height: 60px;
    border-radius: 10px;
    background: linear-gradient(180deg, var(--hive) 0%, var(--hive-deep) 100%);
  }
  .claim {
    top: 186px;
    color: var(--accent);
    font-weight: 600;
    font-size: 16px;
    line-height: 18px;
  }
  .claim__sub {
    display: block;
    font-weight: 600;
    font-size: 11.5px;
    letter-spacing: 0.6px;
    line-height: 15px;
  }
  .gmo {
    top: 223px;
    color: var(--note);
    font-weight: 600;
    font-size: 11px;
    line-height: 16px;
  }
</style>
</head>
<body>
<main class="sheet">

  <section class="ribbon-label ribbon-label--black">
    <div class="band" role="img" aria-label="Honeycomb hexagon pattern on black ribbon"></div>
    <div class="badge">
      <svg width="216" height="262" viewBox="0 0 216 262" aria-hidden="true">
        <polygon class="badge__shape" points="108,0 216,47 216,215 108,262 0,215 0,47"/>
      </svg>
      <p class="badge__text brand-name">Meadowrun<br>Honey</p>
      <div class="hive-art" role="img" aria-label="Beehive with bees and flourishes"></div>
      <p class="badge__text claim">100%<span class="claim__sub">NATURAL HONEY</span></p>
      <p class="badge__text gmo">GMO Free</p>
    </div>
  </section>

  <section class="ribbon-label ribbon-label--red">
    <div class="band" role="img" aria-label="Honeycomb hexagon pattern on red ribbon"></div>
    <div class="badge">
      <svg width="216" height="262" viewBox="0 0 216 262" aria-hidden="true">
        <polygon class="badge__shape" points="108,0 216,47 216,215 108,262 0,215 0,47"/>
      </svg>
      <p class="badge__text brand-name">Meadowrun<br>Honey</p>
      <div class="hive-art" role="img" aria-label="Beehive with bees and flourishes"></div>
      <p class="badge__text claim">100%<span class="claim__sub">NATURAL HONEY</span></p>
      <p class="badge__text gmo">GMO Free</p>
    </div>
  </section>

  <section class="ribbon-label ribbon-label--yellow">
    <div class="band" role="img" aria-label="Honeycomb hexagon pattern on yellow ribbon"></div>
    <div class="badge">
      <svg width="216" height="262" viewBox="0 0 216 262" aria-hidden="true">
        <polygon class="badge__shape" points="108,0 216,47 216,215 108,262 0,215 0,47"/>
      </svg>
      <p class="badge__text brand-name">Meadowrun<br>Honey</p>
      <div class="hive-art" role="img" aria-label="Beehive with bees and flourishes"></div>
      <p class="badge__text claim">100%<span class="claim__sub">NATURAL HONEY</span></p>
      <p class="badge__text gmo">GMO Free</p>
    </div>
  </section>

</main>
</body>
</html>
```